Hi
Thank you for considering my job.

I need a layout design for a website. The design should preferably suit GainsLayout Blogcraft layout. Please design according to the attached LAYOUT.GIF

I already have a logo which I like but could be pushed to change if you have an exceptional design. Otherwise I would like to try to incorporate the jigsaw pieces in the design somehow.

Our company is based in Australia and called Parting Toolbox. We have developed a "Sever Pack" to assist both men and women going through divorce to prepare themselves adequately before the seek legal or financial advice to ensure they pay professionals for "advice" and not instructions on basic administration.

I hope the successful candidate will also be able to design a logo and squeeze page and all of the marketing images I will need to accompany The Sever Pack in a few weeks time, though it is not part of this job.

I have attached a very rough guide as to the types of elements and how I would like it to feel. I am not set on any of the fonts or general presentation at all. I feel comfortable with the colour scheme but again, open to ideas. Although the logo has the dark teal green background, I am not sure this works on the web page - open to ideas.

Some must haves:
a video on the front page
an opt in/members' login
link to Orinoco books sales (affiliate widget)
Disclaimer must be visible on first SCREEN

The website must portray a professional, trustworthy and up to date type image - similar to a law firm, accounting firm, bank or university. It must be clean and crisp, inviting and non-gender biased.

Please message me if you have any questions at all.

Thanks again.
Marguerite
Perth, Australia

Target Market(s)

Australian MEN AND WOMEN - 30 - 60 years middle to upper income earners

Industry/Entity Type

Accounting

Requirements
Must have
• Some must haves:
a video on the front page
an opt in/members' login

The website must portray a professional, trustworthy and up to date type image - similar to a law firm, accounting firm BUT SLIGHTLY MORE PEOPLE ORIENTED

```html
<!DOCTYPE html>
<html lang="en">
<head>
<meta charset="utf-8">
<title>Parting Toolbox</title>
<link rel="stylesheet" href="https://fonts.googleapis.com/css2?family=Noto+Serif:ital,wght@0,400;0,700;1,400;1,700&family=Open+Sans:wght@300;400;600;700&display=swap">
<style>
:root{
  --teal-dark:#033e55;
  --teal-text:#0b4a63;
  --cyan:#7fe3ef;
  --cyan-link:#8fe6f2;
  --orange:#ff6a3d;
  --grey-text:#7a7a7a;
  --rule:#c9c9c9;
  --white:#ffffff;
}
*{box-sizing:border-box;margin:0;padding:0}
html,body{width:1191px;height:1200px;overflow:hidden}
body{position:relative;font-family:"Open Sans",Arial,sans-serif;background:linear-gradient(#ececec 0,#f6f6f6 600px,#fff 1000px);color:var(--teal-text)}
.abs{position:absolute}
.serif{font-family:"Noto Serif",Georgia,serif}
.nowrap{white-space:nowrap}

/* header */
.site-header{left:0;top:0;width:1191px;height:138px;background:var(--teal-dark)}
.brand-mark{left:79px;top:38px;width:60px;height:60px;background:var(--cyan);border-radius:4px}
.brand-name{left:251px;top:40px;font-size:38px;font-weight:300;color:var(--white);letter-spacing:-.3px;line-height:1}
.brand-tagline{left:252px;top:82px;font-size:16px;font-weight:300;color:var(--white);line-height:1.2}
.login-field{top:29px;height:21px;background:var(--white);font-size:11px;color:#555;padding:3px 5px}
.login-btn{left:1087px;top:29px;width:61px;height:21px;background:var(--cyan);color:var(--teal-dark);font-size:13px;text-align:center;line-height:21px}
.login-links{left:890px;top:56px;font-size:11px;color:var(--cyan-link)}
.login-links .remember{color:var(--white);margin-left:10px}
.remember-box{display:inline-block;width:8px;height:8px;background:var(--white);margin-right:3px}
.register{left:889px;top:83px;font-size:12px;color:var(--white)}
.register span{color:var(--cyan-link)}
.register-note{left:889px;top:98px;font-size:10px;color:var(--white)}

/* nav */
.main-nav{top:150px;font-size:13px;color:var(--teal-dark);white-space:nowrap}
.search{left:986px;top:147px;width:93px;height:21px;background:var(--white);font-size:11px;color:#666;padding:3px 6px}
.social{top:147px;width:22px;height:22px}

/* content panel */
.content{left:42px;top:176px;width:1107px;height:994px;background:var(--white)}
.video-heading{left:79px;top:204px;font-size:30px;font-style:italic;font-weight:400;color:var(--teal-dark)}
.promo{left:77px;top:255px;width:391px;height:279px;background:var(--teal-dark);padding:14px 18px;color:var(--white)}
.promo-lead{font-size:20.5px;font-style:italic;line-height:27px;white-space:nowrap}
.promo-lead em{color:var(--orange)}
.promo-body{font-size:15px;line-height:22px;margin-top:16px;white-space:nowrap}
.promo-more{position:absolute;left:18px;bottom:12px;font-size:16px;color:var(--cyan-link)}
.video{left:483px;top:255px;width:370px;height:279px;background:radial-gradient(circle at 40% 45%,#f3dccb 0,#e8c5ad 25%,#cfd9b6 55%,#e9efe0 100%)}

/* articles */
.articles{left:77px;top:551px;width:776px;height:445px;background:linear-gradient(#ebebeb,#fdfdfd)}
.scrollbar{left:840px;top:551px;width:13px;height:445px;background:#dcdcdc}
.scroll-thumb{left:843px;top:670px;width:7px;height:60px;background:var(--white)}
.article{left:95px;width:735px}
.article h3{font-size:19px;font-style:italic;font-weight:700;color:var(--teal-dark);line-height:24px}
.article time{display:block;font-size:15px;font-style:italic;font-weight:700;color:var(--teal-dark);line-height:20px}
.article p{font-size:14.5px;line-height:20px;color:var(--grey-text);margin-top:4px}
.article p a{color:var(--teal-dark)}

/* callouts */
.callout{top:1008px;height:69px;padding:12px 19px;color:var(--teal-dark);overflow:hidden}
.callout-tool{left:77px;width:378px;background:var(--cyan)}
.callout-space{left:475px;width:378px;background:var(--orange)}
.callout .big{font-size:19px;line-height:22px;font-weight:300}
.callout .big b{font-weight:600}
.callout .small{font-size:13.5px;line-height:18px}
.book-strip{left:886px;top:1008px;width:245px;height:70px;background:linear-gradient(90deg,#4a4f5a,#c74a3a 30%,#2d3a55 55%,#b23030 75%,#1d4a5a)}

/* sidebar */
.testimonial{left:889px;top:204px;width:250px;font-size:23px;font-style:italic;line-height:28px;color:var(--orange);white-space:nowrap}
.rule{left:889px;width:239px;height:1px;background:var(--rule)}
.join{left:889px;top:360px;font-size:21px;color:var(--teal-dark);font-weight:300}
.perks{left:889px;top:395px;width:245px;list-style:none;font-size:14px;line-height:19px;color:var(--teal-dark)}
.perks li{position:relative;padding-left:20px;margin-bottom:9px}
.perks li::before{content:"";position:absolute;left:2px;top:4px;width:11px;height:11px;background:var(--teal-dark)}
.buy{left:889px;top:548px;font-size:23px;font-style:italic;color:var(--orange)}
.price{left:889px;top:581px;font-size:17px;font-weight:700;color:var(--orange)}
.book{left:889px;top:627px;width:242px;height:217px;background:linear-gradient(160deg,#1f5a6a,#0f4254 60%,#d8d8d8 61%)}
.book-copy{left:889px;top:864px;width:245px;font-size:14.5px;line-height:20px;color:var(--grey-text)}
.book-copy a{color:var(--teal-dark)}

/* footer */
.disclaimer{left:0;width:1191px;top:1156px;text-align:center;font-size:12px;color:#333}
.footer-links{left:0;width:1191px;top:1180px;text-align:center;font-size:11px;color:var(--teal-dark)}
.footer-links span{margin:0 14px}
</style>
</head>
<body>

<header class="abs site-header">
  <div class="abs brand-mark"></div>
  <div class="abs brand-name">partingtoolbox</div>
  <div class="abs brand-tagline">guidance for each step ahead</div>

  <div class="abs login-field" style="left:890px;width:93px">Username</div>
  <div class="abs login-field" style="left:989px;width:90px">Password</div>
  <div class="abs login-btn">LOG IN</div>
  <div class="abs login-links">FORGET LOGIN? <span class="remember"><span class="remember-box"></span>REMEMBER</span></div>
  <div class="abs register">Not accout yet? <span>REGISTER FOR FREE TODAY</span></div>
  <div class="abs register-note">Do not use your name as username</div>
</header>

<nav>
  <span class="abs main-nav" style="left:77px">HOME</span>
  <span class="abs main-nav" style="left:137px">CONSIDERING DIVORCE</span>
  <span class="abs main-nav" style="left:298px">LEGAL PROCESS</span>
  <span class="abs main-nav" style="left:419px">PARENTING</span>
  <span class="abs main-nav" style="left:509px">PROPERTY &amp; FINANCE</span>
  <span class="abs main-nav" style="left:659px">COMMUNITY</span>
  <span class="abs main-nav" style="left:761px">TOOLS</span>
  <span class="abs main-nav" style="left:825px">FAQS</span>
  <span class="abs main-nav" style="left:878px">ABOUT US</span>
  <div class="abs search">Search</div>
  <div class="abs social" style="left:1096px;background:#3b5a98"></div>
  <div class="abs social" style="left:1127px;background:#45b0e3"></div>
</nav>

<main class="abs content"></main>

<h1 class="abs video-heading serif">Click to play the Video Guide (image below)</h1>

<section class="abs promo">
  <p class="promo-lead serif"><em>The Sever Pack</em> Fake text. Thank for<br>using Marks of the Globe your<br>logo needs. This site is made<br>possible thanks to contributions</p>
  <p class="promo-body">From people like you who upload vector logos<br>for designers, so we can reproduce brands oln<br>artworkscorrectly and with high quality. Please<br>consider uploading any vector logos that</p>
  <span class="promo-more">CLICK TO LEARN MORE</span>
</section>

<div class="abs video" role="img" aria-label="Video guide still: photo of a smiling woman">
  <svg width="370" height="279" style="position:absolute;left:0;top:0">
    <circle cx="185" cy="143" r="27" fill="#033e55"/>
    <path d="M177 129 L197 143 L177 157 Z" fill="#fff"/>
  </svg>
</div>

<section class="abs articles"></section>
<div class="abs scrollbar"></div>
<div class="abs scroll-thumb"></div>

<article class="abs article" style="top:563px">
  <h3 class="serif">Article 04 (title)</h3><time class="serif">Apr. 2013</time>
  <p>This site is made possible thanks to contributions frm people like you who uploadontributions from people like you who upload This site is &nbsp;vector logos for designers, so we can... <a>+ READ MORE</a></p>
</article>
<article class="abs article" style="top:673px">
  <h3 class="serif">Article 03 (title)</h3><time class="serif">Mar. 2013</time>
  <p>This site is made possible thanks to contributions frm people like you who uploadontributions from people like you who upload This site is &nbsp;vector logos for designerrmn... <a>+ READ MORE</a></p>
</article>
<article class="abs article" style="top:783px">
  <h3 class="serif">Article 02 (title)</h3><time class="serif">Feb. 2013</time>
  <p>This site is made possible thanks to contributions frm people like you who uploadontributions from people like you who upload This site is &nbsp;vector logos for designers, so we can... <a>+ READ MORE</a></p>
</article>
<article class="abs article" style="top:889px">
  <h3 class="serif">Article 01 (title)</h3><time class="serif">Jan. 2013</time>
  <p>This site is made possible thanks to contributions frm people like you who uploadontributions from people like you who upload This site is &nbsp;vectan... <a>+ READ MORE</a></p>
</article>

<div class="abs callout callout-tool">
  <div class="big">TRY OUR <b>FREE DIVORCE TOOL</b></div>
  <div class="small">From people you who upload.</div>
</div>
<div class="abs callout callout-space">
  <div class="big">FREE SPACE IN CASE<br>YOU NEED</div>
</div>
<div class="abs book-strip" role="img" aria-label="Orinoco book sales widget showing a row of book covers"></div>

<aside>
  <blockquote class="abs testimonial serif">“Testimonials in order<br>to entice the person<br>to stay on the website,<br>testimonials...”</blockquote>
  <div class="abs rule" style="top:340px"></div>
  <h2 class="abs join">JOIN OUR COMMUNITY</h2>
  <ul class="abs perks">
    <li>Free membership</li>
    <li>Instant free access &nbsp;to calculators and resources</li>
    <li>Anonymous participation<br>in support and advice forums</li>
  </ul>
  <div class="abs rule" style="top:530px"></div>
  <div class="abs buy serif">Buy Now!</div>
  <div class="abs price">$ 12.99</div>
  <div class="abs book" role="img" aria-label="Cover of the printed Sever Pack guide book"></div>
  <p class="abs book-copy">Download Immediately. This simple guide provides a wealth of essential information and answers to your questions. Advice and tips to help you get a grip on all the changes in your life. <a>+ READ MORE</a></p>
</aside>

<footer>
  <p class="abs disclaimer">Disclaimer fake text Disclaimer fake text Disclaimer fake text Disclaimer fake text Disclaimer fake text Disclaimer fake text Disclaimer fake text</p>
  <p class="abs footer-links"><span>CONTACTS</span><span>PRIVACY POLICY</span><span>DISCLAIMER</span></p>
</footer>

</body>
</html>
```